KELVARA Branded Wellness Pouch Design for Clinical Study Kit

Overview:
We are creating custom zippered pouches for our “KELVARA Study Fuel Kits,” which will be distributed to physicians, nurses, and research coordinators participating in a national clinical study. We need a clean, professional design for the front of the pouch that incorporates our existing KELVARA logo and the new supporting text.
Design Requirements:
Keep the existing KELVARA logo intact (we’ll upload the file).
Add the text “Study Fuel Kit” immediately following the logo, using the same or a complementary font.
Add a tagline below that reads:
Power up. Kelvara. Go again.
Use a layout that looks balanced, legible, and polished when printed on a small pouch.
Stay consistent with our brand color palette (blue from the logo)
The overall style should feel modern, wellness-driven, and professional — think premium, science-forward, and sleek.
Audience:
This kit will be given to medical professionals, so the design should feel elevated and credible (not flashy or overly playful).
Deliverables:
Vector file (AI, EPS)
It is a frosted white, zippered vinyl pouch (9 1/2 " x 8 1/4 " x 2 1/2 ")
The imprint size is (6 3/4" W x 4 1/2" H)
The imprint can only be 1-color, so in this case - we would like the color to be the dark blue (#06173c)

```html
<!DOCTYPE html>
<html lang="en">
<head>
<meta charset="utf-8">
<title>KELVARA Study Fuel Kit – Pouch Imprint</title>
<link rel="stylesheet" href="https://fonts.googleapis.com/css2?family=Bebas+Neue&family=Encode+Sans+Condensed:wght@500;600&display=swap">
<style>
  :root {
    --ink: #06173c;
    --paper: #ffffff;
  }
  html, body {
    margin: 0;
    padding: 0;
    width: 1200px;
    height: 1200px;
    overflow: hidden;
    background: var(--paper);
  }
  .canvas {
    position: relative;
    width: 1200px;
    height: 1200px;
    background: var(--paper);
  }
  .imprint {
    position: absolute;
    left: 394px;
    top: 462px;
    width: 412px;
    height: 275px;
    box-sizing: border-box;
    border: 1px solid var(--ink);
    background: var(--paper);
    color: var(--ink);
  }
  .stripe-band {
    position: absolute;
    left: 0;
    right: 0;
    background: var(--ink);
  }
  .stripe-band--top { top: 0; height: 49px; }
  .stripe-band--bottom { bottom: 0; height: 70px; }

  .brand {
    position: absolute;
    left: 0;
    right: 0;
    top: 56px;
    text-align: center;
  }
  .brand-name {
    display: block;
    font-family: "Encode Sans Condensed", "Arial Narrow", sans-serif;
    font-weight: 500;
    font-size: 64px;
    line-height: 1;
    letter-spacing: 0.5px;
    color: var(--ink);
  }
  .brand-descriptor {
    display: block;
    margin: 3px 0 0 96px;
    text-align: right;
    width: 269px;
    font-family: "Encode Sans Condensed", "Arial Narrow", sans-serif;
    font-weight: 600;
    font-size: 7.2px;
    line-height: 1;
    color: var(--ink);
    white-space: nowrap;
  }
  .kit-title,
  .tagline {
    position: absolute;
    left: 0;
    right: 0;
    margin: 0;
    text-align: center;
    font-family: "Bebas Neue", "Oswald", sans-serif;
    font-weight: 400;
    line-height: 1;
    color: var(--ink);
  }
  .kit-title {
    top: 134px;
    font-size: 34px;
    letter-spacing: 0.3px;
  }
  .tagline {
    top: 171px;
    font-size: 35px;
    letter-spacing: 0.3px;
  }
</style>
</head>
<body>
  <main class="canvas">
    <section class="imprint" aria-label="KELVARA Study Fuel Kit pouch imprint">
      <div class="stripe-band stripe-band--top" role="img" aria-label="Vertical stripe pattern band in dark blue"></div>

      <div class="brand">
        <span class="brand-name">KELVARA U.S.</span>
        <span class="brand-descriptor">NOVA Disc Randomized, Sham-Controlled, Multi-Center, Double Blind Clinical Trial</span>
      </div>

      <h1 class="kit-title">Study Fuel Kit</h1>
      <p class="tagline">Power up. Kelvara. Go again.</p>

      <div class="stripe-band stripe-band--bottom" role="img" aria-label="Vertical stripe pattern band in dark blue"></div>
    </section>
  </main>
</body>
</html>
```